Winter Fence Sale Fence Types

Please create a flyer, similar to what we did previous, but mimicking this page listing the fence styles: http://bramblewoodrails.com/snowfall-deal-2019

Industry/Entity Type

Residential Construction

Font styles to use
Sans Serif

Colors
cee9f5
33a6d7
d0dfed

Requirements
Must have
• Fence styles and photo of fence styles
Nice to have
• Phone number, address, logo

```html
<!DOCTYPE html>
<html lang="en">
<head>
<meta charset="utf-8">
<title>Bramblewood Rails – Winter Fence Sales</title>
<link href="https://fonts.googleapis.com/css2?family=Bebas+Neue&family=Roboto:wght@300;400;700;900&display=swap" rel="stylesheet">
<style>
:root{
  --blue:#3f86c8;
  --blue-dark:#2f6fae;
  --ink:#141414;
  --white:#ffffff;
  --red:#e3262b;
}
*{margin:0;padding:0;box-sizing:border-box}
html,body{width:1101px;height:1200px;overflow:hidden;background:var(--white)}
body{font-family:'Roboto',sans-serif;color:var(--ink)}
.flyer{position:relative;width:1101px;height:1200px;overflow:hidden}

/* header */
.header{position:absolute;left:0;top:0;width:1101px;height:148px;background:var(--white)}
.brand-mark{position:absolute;left:32px;top:32px;width:80px;height:80px;background:#5a3a22}
.brand-name{position:absolute;left:130px;top:26px;font-weight:700;font-size:40px;color:var(--blue);letter-spacing:.5px}
.brand-phone{position:absolute;left:130px;top:70px;font-weight:900;font-size:38px;color:var(--ink)}
.brand-tagline{position:absolute;left:130px;top:116px;font-weight:700;font-size:14px;color:var(--ink)}
.contact-panel{position:absolute;left:580px;top:0;width:521px;height:142px;background:var(--blue);clip-path:polygon(9% 0,100% 0,100% 100%,0 100%);color:var(--white);text-align:right;padding:12px 22px 0 0}
.contact-phone{font-weight:900;font-size:40px;line-height:44px;display:flex;justify-content:flex-end;align-items:center;gap:14px}
.contact-line{font-weight:300;font-size:28px;line-height:33px}
.contact-line.with-pin{display:flex;justify-content:flex-end;align-items:center;gap:12px}
.contact-note{font-size:13px;line-height:16px;margin-top:2px}

/* hero */
.hero{position:absolute;left:0;top:148px;width:1101px;height:262px;background:linear-gradient(180deg,#1d2f55 0%,#121a2c 45%,#3a3129 100%);color:var(--white)}
.hero-title{position:absolute;left:0;right:0;top:10px;text-align:center;font-family:'Bebas Neue',sans-serif;font-size:92px;line-height:1;letter-spacing:1px;font-weight:400}
.hero-sub{position:absolute;left:0;right:0;top:98px;text-align:center;font-weight:300;font-size:30px}
.offer-box{position:absolute;top:140px;height:116px;border:2px dashed var(--white);font-family:'Bebas Neue',sans-serif;display:flex;align-items:center;justify-content:center;gap:14px}
.offer-price{left:60px;width:463px}
.offer-visit{left:590px;width:465px}
.offer-lead{font-size:44px;line-height:.85;text-align:center}
.offer-lead small{display:block;font-size:26px}
.offer-big{font-size:100px;line-height:1}
.offer-big span{font-size:44px}
.offer-stack{display:flex;flex-direction:column;align-items:center;margin-top:-6px}
.offer-open{font-size:28px;line-height:1;margin-bottom:-8px}
.offer-visit .offer-big{font-size:92px}
.divider{position:absolute;left:548px;top:284px;width:3px;height:510px;background:#d9d9d9}

/* style grid */
.styles{position:absolute;left:0;top:410px;width:1101px;height:395px;background:var(--blue)}
.photo{position:absolute;width:239px;height:120px}
.ph-wood{background:linear-gradient(135deg,#c9a874 0%,#e6cfa2 50%,#8d7350 100%)}
.ph-yard{background:linear-gradient(135deg,#7b6a4c 0%,#d7bd8c 55%,#5e7a3f 100%)}
.ph-grass{background:linear-gradient(180deg,#3f6a35 0%,#d8c08f 60%,#6b8f43 100%)}
.style-tab{position:absolute;width:200px;margin-left:-100px;background:var(--blue);color:var(--white);font-size:21px;text-align:center;padding:2px 0 4px;border-radius:0 0 3px 3px}

/* price rows */
.price-area{position:absolute;left:0;top:805px;width:884px;height:291px;background:var(--ink);color:var(--white)}
.price-heading{position:absolute;left:0;right:0;text-align:center;font-size:28px;font-weight:400}
.thumb{position:absolute;width:162px;height:70px}
.caption{position:absolute;width:162px;text-align:center;font-size:13px;line-height:15px}
.wire-panel{position:absolute;left:884px;top:805px;width:217px;height:291px;background:var(--blue)}
.wire-tab{position:absolute;left:12px;top:6px;width:193px;background:var(--white);color:var(--blue);font-size:22px;text-align:center;padding:2px 0}
.wire-photo{position:absolute;left:12px;top:46px;width:193px;height:238px;background:linear-gradient(180deg,#dfe6ea 0%,#c7d3d6 30%,#3e6b33 50%,#7ea04f 100%)}

/* footer */
.footer{position:absolute;left:0;top:1096px;width:1101px;height:104px;background:var(--white)}
.hours{position:absolute;left:12px;top:10px;display:flex;align-items:center;gap:8px}
.hours-label{font-family:'Bebas Neue',sans-serif;font-size:30px;line-height:.9;color:var(--blue)}
.hours-col{font-family:'Bebas Neue',sans-serif;text-align:center;line-height:1}
.hours-day{font-family:'Roboto',sans-serif;font-weight:700;font-style:italic;font-size:12px}
.hours-time{font-size:36px}
.hours-closed{position:absolute;left:222px;top:58px;color:var(--red);font-weight:700;font-size:15px}
.tagline-strip{position:absolute;left:0;top:76px;width:555px;height:28px;background:var(--blue);color:var(--white);font-size:18px;letter-spacing:3px;padding:3px 0 0 46px;clip-path:polygon(0 0,100% 0,97% 100%,0 100%)}
.web-panel{position:absolute;left:540px;top:8px;width:561px;height:96px;background:var(--blue);clip-path:polygon(5% 0,100% 0,100% 100%,0 100%);color:var(--white);padding:12px 0 0 50px}
.web-line{display:flex;align-items:center;gap:14px;font-size:22px;font-weight:400;line-height:34px}
.dot{width:22px;height:22px;border-radius:50%;background:var(--white)}
</style>
</head>
<body>
<div class="flyer">

  <header class="header">
    <div class="brand-mark"></div>
    <div class="brand-name">Bramblewood Rails</div>
    <div class="brand-phone">704-555-0142</div>
    <div class="brand-tagline">“Because Good Fences Make Good Neighbors”</div>
    <div class="contact-panel">
      <div class="contact-phone">
        <svg width="34" height="34" viewBox="0 0 24 24"><path fill="#fff" d="M6.6 10.8a15.1 15.1 0 006.6 6.6l2.2-2.2a1 1 0 011-.25 11.4 11.4 0 003.6.6 1 1 0 011 1V20a1 1 0 01-1 1A17 17 0 013 4a1 1 0 011-1h3.5a1 1 0 011 1c0 1.25.2 2.45.6 3.6a1 1 0 01-.25 1z"/></svg>
        704-555-0142
      </div>
      <div class="contact-line">418 Orchard Ln</div>
      <div class="contact-line with-pin">
        <svg width="20" height="28" viewBox="0 0 22 30"><path fill="#fff" d="M11 0a11 11 0 00-11 11c0 8 11 19 11 19s11-11 11-19A11 11 0 0011 0zm0 15a4 4 0 110-8 4 4 0 010 8z"/></svg>
        Millbrook, NC 28199
      </div>
      <div class="contact-note">Minutes From Cedar Ridge!</div>
    </div>
  </header>

  <section class="hero" role="img" aria-label="Evening photo of a wooden picket privacy fence beside a house">
    <h1 class="hero-title">WINTER FENCE SALES</h1>
    <p class="hero-sub">Welcome to our Winter Fence Sale!</p>
    <div class="offer-box offer-price">
      <div class="offer-lead">WOOD FENCES<br>STARTING AT</div>
      <div class="offer-big">$12<span>/FT!</span></div>
    </div>
    <div class="offer-box offer-visit">
      <div class="offer-lead">COME VISIT<small>OUR OUTDOOR SHOWROOM</small></div>
      <div class="offer-stack">
        <div class="offer-open">OPEN</div>
        <div class="offer-big">24/7</div>
      </div>
    </div>
  </section>

  <section class="styles">
    <div class="photo ph-wood"  style="left:25px;top:10px"  role="img" aria-label="2 rail split rail fence with gate"></div>
    <div class="photo ph-yard"  style="left:289px;top:10px" role="img" aria-label="2 rail split rail fence along a garden path"></div>
    <div class="photo ph-yard"  style="left:574px;top:10px" role="img" aria-label="2 rail estate rail fence with gate"></div>
    <div class="photo ph-wood"  style="left:837px;top:10px" role="img" aria-label="2 rail estate rail fence with wire"></div>

    <div class="photo ph-wood"  style="left:25px;top:142px"  role="img" aria-label="Dog ear picket fence corner"></div>
    <div class="photo ph-wood"  style="left:289px;top:142px" role="img" aria-label="Dog ear picket fence with garden plants"></div>
    <div class="photo ph-wood"  style="left:574px;top:142px" role="img" aria-label="French gothic picket fence with gate"></div>
    <div class="photo ph-grass" style="left:837px;top:142px" role="img" aria-label="French gothic picket fence around a patio"></div>

    <div class="photo ph-wood"  style="left:25px;top:274px"  role="img" aria-label="Sunrise picket fence with arched gate"></div>
    <div class="photo ph-yard"  style="left:289px;top:274px" role="img" aria-label="Sunrise picket fence along a path"></div>
    <div class="photo ph-grass" style="left:574px;top:274px" role="img" aria-label="Sunset picket fence on a lawn"></div>
    <div class="photo ph-grass" style="left:837px;top:274px" role="img" aria-label="Sunset picket fence along a yard"></div>

    <div class="style-tab" style="left:272px;top:0">2 Rail Split Rail</div>
    <div class="style-tab" style="left:825px;top:0;width:230px;margin-left:-115px">2 Rail Estate Rail</div>
    <div class="style-tab" style="left:272px;top:132px">Dog Ear Picket</div>
    <div class="style-tab" style="left:825px;top:132px;width:230px;margin-left:-115px">French Gothic Picket</div>
    <div class="style-tab" style="left:272px;top:264px">Sunrise Picket</div>
    <div class="style-tab" style="left:825px;top:264px">Sunset Picket</div>
  </section>

  <div class="divider"></div>

  <section class="price-area">
    <h2 class="price-heading" style="top:6px">$14/FT FENCE STYLES</h2>
    <div class="thumb ph-wood" style="left:20px;top:44px"  role="img" aria-label="Dog ear privacy fence"></div>
    <div class="thumb ph-wood" style="left:192px;top:44px" role="img" aria-label="Sunrise privacy fence"></div>
    <div class="thumb ph-wood" style="left:364px;top:44px" role="img" aria-label="Sunset privacy fence"></div>
    <div class="thumb ph-yard" style="left:536px;top:44px" role="img" aria-label="3 rail estate rail fence with wire"></div>
    <div class="thumb ph-grass" style="left:708px;top:44px" role="img" aria-label="3 rail split rail fence with wire"></div>
    <div class="caption" style="left:20px;top:118px">Dog Ear Privacy</div>
    <div class="caption" style="left:192px;top:118px">Sunrise Privacy</div>
    <div class="caption" style="left:364px;top:118px">Sunset Privacy</div>
    <div class="caption" style="left:536px;top:118px">3 Rail Estate Rail with wire</div>
    <div class="caption" style="left:708px;top:118px">3 Rail Split Rail with wire</div>

    <h2 class="price-heading" style="top:140px">$16/FT FENCE STYLES</h2>
    <div class="thumb ph-yard" style="left:20px;top:178px"  role="img" aria-label="4 rail estate rail fence with wire"></div>
    <div class="thumb ph-wood" style="left:192px;top:178px" role="img" aria-label="Shadowbox fence"></div>
    <div class="thumb ph-wood" style="left:364px;top:178px" role="img" aria-label="Sunrise shadowbox fence"></div>
    <div class="thumb ph-grass" style="left:536px;top:178px" role="img" aria-label="Sunset shadowbox fence"></div>
    <div class="thumb ph-wood" style="left:708px;top:178px" role="img" aria-label="Top cap privacy fence"></div>
    <div class="caption" style="left:20px;top:252px">4 Rail Estate Rail<br>with Wire</div>
    <div class="caption" style="left:192px;top:252px">Shadowbox</div>
    <div class="caption" style="left:364px;top:252px">Sunrise Shadowbox</div>
    <div class="caption" style="left:536px;top:252px">Sunset Shadowbox</div>
    <div class="caption" style="left:708px;top:252px">Top Cap</div>
  </section>

  <aside class="wire-panel">
    <div class="wire-tab">Post and Wire</div>
    <div class="wire-photo" role="img" aria-label="Post and wire fence across an open field"></div>
  </aside>

  <footer class="footer">
    <div class="hours">
      <svg width="44" height="42" viewBox="0 0 44 42"><rect x="2" y="6" width="34" height="30" rx="3" fill="none" stroke="#3f86c8" stroke-width="3"/><rect x="2" y="6" width="34" height="8" fill="#3f86c8"/><rect x="9" y="1" width="4" height="9" fill="#3f86c8"/><rect x="25" y="1" width="4" height="9" fill="#3f86c8"/><circle cx="34" cy="32" r="9" fill="#fff" stroke="#3f86c8" stroke-width="3"/><path d="M34 27v5h4" stroke="#3f86c8" stroke-width="2.5" fill="none"/></svg>
      <div class="hours-label">OFFICE<br>HOURS</div>
      <svg width="14" height="24" viewBox="0 0 14 24"><path d="M2 2l9 10-9 10" stroke="#3f86c8" stroke-width="4" fill="none"/></svg>
      <div class="hours-col"><div class="hours-day">MONDAY TO THURSDAY</div><div class="hours-time">9 AM TO 3 PM</div></div>
      <div class="hours-col" style="margin-left:24px"><div class="hours-day">FRIDAY</div><div class="hours-time">9 AM TO 3 PM</div></div>
    </div>
    <div class="hours-closed">CLOSED 11:30 - 12:30 PM</div>
    <div class="tagline-strip">MANY FENCE STYLES AVAILABLE</div>
    <div class="web-panel">
      <div class="web-line">
        <svg width="24" height="24" viewBox="0 0 24 24"><circle cx="12" cy="12" r="10" fill="none" stroke="#fff" stroke-width="2"/><ellipse cx="12" cy="12" rx="4.5" ry="10" fill="none" stroke="#fff" stroke-width="2"/><path d="M2 12h20" stroke="#fff" stroke-width="2"/></svg>
        www.BramblewoodRails.com
      </div>
      <div class="web-line"><span class="dot"></span>Follow.us/BramblewoodRails</div>
    </div>
  </footer>

</div>
</body>
</html>
```